UK Glass Restoration Company needs a Direct Mail Postcard Design

We need a HARD HITTING, COMPELLING 300dpi Camera Ready double sided postcard.
The dimensions will be 109mm x 152mm including bleed. We are a scratched glass repair / etched graffiti removal glass restoration company based in London, UK.
We operate mainly within the construction and commercial marketplace, however this particular postcard design is aimed solely at shop owners who have become victims of vandalism, due to etched graffiti tags and or scratches being left on their shop front glass.
We wish to focus the shop / business owners mind to the negative impact such vandalism has on the image of their business and how we are able to offer a quick and cost effective solution
We will supply text for both sides of the postcard along with relevant images, company logo and previous flyer designs, however we are happy for the selected designer to source suitable alternative images provided they are in keeping with the exact "Before" and "After" theme.
The finished postcard must preferably have a white background, but again we are open to creative suggestions.
Target Market(s)
UK SHOP OWNERS
Industry/Entity Type
It Company

```html
<!DOCTYPE html>
<html lang="en">
<head>
<meta charset="utf-8">
<title>Lumen Glass Care – Postcard</title>
<link rel="stylesheet" href="https://fonts.googleapis.com/css2?family=Arimo:wght@400;700&family=Open+Sans:wght@400;600;700&family=Roboto+Condensed:wght@700&family=Tinos:wght@400;700&display=swap">
<style>
  :root{
    --page:#e9e7e4;
    --blue-light:#2a86bf;
    --blue-dark:#0c4670;
    --brand:#1d8bd0;
    --red:#e2142d;
    --grey-text:#4a4a4a;
    --swoosh:#c9c4c6;
    --ink:#111;
    --white:#fff;
  }
  *{box-sizing:border-box;margin:0;padding:0}
  html,body{width:900px;height:1200px;overflow:hidden;background:var(--page)}
  .canvas{position:relative;width:900px;height:1200px}
  .postcard{position:absolute;left:112px;width:676px;height:485px;overflow:hidden;box-shadow:0 6px 18px rgba(0,0,0,.25);font-family:"Open Sans",Arial,sans-serif;color:var(--white)}
  .postcard--front{top:85px}
  .postcard--back{top:650px}
  .postcard__shapes{position:absolute;inset:0}
  .abs{position:absolute}
  .brand-name{font-family:"Open Sans",Arial,sans-serif;font-weight:400;color:var(--brand);font-size:31px;letter-spacing:.3px;white-space:nowrap}
  .headline{left:150px;width:370px;text-align:center;font-family:"Arimo",Arial,sans-serif;line-height:1}
  .headline--alert{top:92px;color:var(--red);font-weight:700;font-size:20px}
  .headline--image{top:118px;color:var(--grey-text);font-size:24px;font-weight:400}
  .intro{left:33px;top:196px;width:330px;font-size:11.4px;line-height:15px;text-align:justify}
  .call-label{left:33px;top:326px;font-family:"Arimo",Arial,sans-serif;font-weight:700;font-size:19px}
  .call-number{left:48px;top:356px;font-family:"Arimo",Arial,sans-serif;font-weight:700;font-size:31px}
  .contact-pill{left:36px;top:408px;color:var(--grey-text);font-size:13px;line-height:24px}
  .contact-row{display:flex;align-items:center;gap:12px}
  .contact-row svg{width:12px;height:12px;flex:none}
  .badge{width:112px;text-align:center;font-family:"Roboto Condensed","Arial Narrow",sans-serif;font-weight:700;color:var(--red);font-size:15px;line-height:17px;text-transform:uppercase}
  .why-title{left:40px;top:140px;font-weight:700;font-size:17px;line-height:20px}
  .benefits{left:32px;top:165px;width:366px;list-style:none;font-size:10.2px;line-height:12px}
  .benefits li{position:relative;padding-left:14px;margin-bottom:5px;text-align:justify}
  .benefits li.benefit--short{width:310px}
  .benefits li::before{content:"";position:absolute;left:0;top:3px;width:7px;height:7px;border-radius:50%;background:var(--white)}
  .back-contact{left:36px;top:336px;font-size:16px;line-height:21px}
  .back-contact .contact-row:last-child{font-size:13px}
  .coupon{left:0;top:390px;width:400px;text-align:center;color:var(--ink);font-family:"Tinos","Times New Roman",serif;font-size:13.5px;line-height:18px}
  .coupon__save{color:var(--blue-dark);font-weight:700;font-size:20px}
  .coupon__off{font-weight:700}
  .coupon__expiry{display:block;text-align:left;padding-left:36px;font-weight:700}
</style>
</head>
<body>
<main class="canvas">

  <section class="postcard postcard--front">
    <svg class="postcard__shapes" viewBox="0 0 676 485" width="676" height="485">
      <defs>
        <linearGradient id="panelBlue" x1="0" y1="0" x2="0" y2="1">
          <stop offset="0" stop-color="#2a86bf"/><stop offset="1" stop-color="#0c4670"/>
        </linearGradient>
        <linearGradient id="photoTone" x1="0" y1="0" x2="1" y2="1">
          <stop offset="0" stop-color="#6b5644"/><stop offset=".5" stop-color="#9a8c7c"/><stop offset="1" stop-color="#4e3a2b"/>
        </linearGradient>
        <linearGradient id="headWhite" x1="0" y1="0" x2="0" y2="1">
          <stop offset="0" stop-color="#fff"/><stop offset="1" stop-color="#eeeeee"/>
        </linearGradient>
      </defs>
      <rect width="676" height="485" fill="url(#panelBlue)"/>
      <path role="img" aria-label="Photo of a shop window with scratched glass over property listings" d="M398,180 C430,130 540,100 676,78 V485 H384 C376,380 378,270 398,180 Z" fill="url(#photoTone)"/>
      <path d="M398,180 C378,270 376,380 384,485" fill="none" stroke="#111" stroke-width="7"/>
      <path d="M0,38 C120,150 260,190 390,178 C480,165 580,95 676,62 V90 C580,118 490,180 392,194 C260,212 110,170 0,70 Z" fill="#111"/>
      <path d="M0,28 C120,140 260,180 390,168 C480,155 580,88 676,52 V80 C580,110 490,172 392,184 C260,200 110,160 0,60 Z" fill="#c9c4c6"/>
      <path d="M0,0 H676 V52 C580,88 480,155 390,168 C260,180 120,140 0,28 Z" fill="url(#headWhite)"/>
      <path d="M28,408 H275 A25,25 0 0 1 275,458 H28 Z" fill="#fff" opacity=".95"/>
      <circle cx="80" cy="85" r="72" fill="#1d8bd0"/>
      <circle cx="80" cy="85" r="63" fill="#fff"/>
      <circle role="img" aria-label="Photo of a technician in hi-vis vest polishing a window" cx="80" cy="85" r="59" fill="#4b5a52"/>
      <circle cx="355" cy="345" r="60" fill="#e2142d"/>
      <circle cx="355" cy="345" r="52" fill="#fff"/>
      <path d="M676,250 H625 V236 L590,270 L625,304 V290 H676 Z" fill="#e2142d"/>
    </svg>

    <div class="abs brand-name" style="left:270px;top:38px">Lumen Glass Care</div>
    <h1 class="abs headline headline--alert">DON'T LET VANDALS WRECK</h1>
    <h2 class="abs headline headline--image">YOUR IMAGE!</h2>

    <p class="abs intro">What's on display in your shop window? If it's graffiti, vandalism, or just wear and tear, that's the first impression your customers get – and it's not good. Lumen Glass Care remove damage from glass windows, making them sparkling clear – without replacing the glass! Our glass repair work is effective, green, and very economical. See our coupon on the other side to save even more!</p>

    <div class="abs call-label">Call now for expert advice</div>
    <div class="abs call-number">0800 555 0142</div>

    <div class="abs contact-pill">
      <div class="contact-row"><svg viewBox="0 0 12 12"><circle cx="6" cy="6" r="5" fill="none" stroke="#0c4670" stroke-width="1.4"/><path d="M1,6 H11 M6,1 V11" stroke="#0c4670" stroke-width="1"/></svg>www.lumenglasscare.co.uk</div>
      <div class="contact-row" style="font-size:15px"><svg viewBox="0 0 12 12"><rect x="1" y="1" width="10" height="10" rx="2" fill="#0c4670"/><path d="M4,3 Q3,6 6,9 L8,8 L7,6.5 L6,7 Q5,6 5,4.5 L5.6,4 Z" fill="#fff"/></svg>0800 555 0142</div>
    </div>

    <div class="abs badge" style="left:299px;top:319px">Before repair<br><span style="font-size:17px">A bad first<br>impression</span></div>
  </section>

  <section class="postcard postcard--back">
    <svg class="postcard__shapes" viewBox="0 0 676 485" width="676" height="485">
      <defs>
        <linearGradient id="panelBlue2" x1="0" y1="0" x2="0" y2="1">
          <stop offset="0" stop-color="#2a86bf"/><stop offset="1" stop-color="#0c4670"/>
        </linearGradient>
        <linearGradient id="photoTone2" x1="0" y1="0" x2="1" y2="1">
          <stop offset="0" stop-color="#6e5a49"/><stop offset=".5" stop-color="#a59888"/><stop offset="1" stop-color="#55412f"/>
        </linearGradient>
      </defs>
      <rect width="676" height="485" fill="url(#panelBlue2)"/>
      <path role="img" aria-label="Photo of the same shop window, now clear after repair" d="M418,130 C470,100 560,70 676,40 V485 H404 C402,360 406,230 418,130 Z" fill="url(#photoTone2)"/>
      <path d="M418,130 C406,230 402,360 404,485" fill="none" stroke="#111" stroke-width="6"/>
      <path d="M0,20 C110,100 230,130 350,126 C460,120 570,62 676,30 V54 C570,82 460,138 350,142 C220,146 100,118 0,50 Z" fill="#111"/>
      <path d="M0,12 C110,92 230,120 350,116 C460,110 570,54 676,22 V44 C570,74 460,128 350,132 C220,136 100,108 0,42 Z" fill="#c9c4c6"/>
      <path d="M0,0 H676 V22 C570,54 460,110 350,116 C230,120 110,92 0,12 Z" fill="#f6f6f6"/>
      <rect x="0" y="382" width="402" height="103" fill="#fff"/>
      <line x1="0" y1="381" x2="402" y2="381" stroke="#111" stroke-width="1.5" stroke-dasharray="6 4"/>
      <g fill="none" stroke="#111" stroke-width="1.6">
        <circle cx="328" cy="376" r="3.5"/><circle cx="328" cy="387" r="3.5"/>
        <path d="M331,378 L350,386 M331,385 L350,377"/>
      </g>
      <circle cx="75" cy="72" r="62" fill="#1d8bd0"/>
      <circle cx="75" cy="72" r="54" fill="#fff"/>
      <circle role="img" aria-label="Photo of a technician in hi-vis jacket working on high-rise glass" cx="75" cy="72" r="50" fill="#6a7458"/>
      <circle cx="410" cy="290" r="58" fill="#e2142d"/>
      <circle cx="410" cy="290" r="50" fill="#fff"/>
      <path d="M676,265 H605 V251 L566,282 L605,313 V299 H676 Z" fill="#e2142d"/>
    </svg>

    <div class="abs brand-name" style="left:270px;top:40px">Lumen Glass Care</div>

    <h2 class="abs why-title">Why Lumen Glass Care?</h2>
    <ul class="abs benefits">
      <li>We repair most shop window glass! We repair laminated, tempered, toughened, mirrored, tinted, and even ballistic glass.</li>
      <li>We repair curved glass! Don't replace expensive curved panes – get the like-new look for less by repairing.</li>
      <li class="benefit--short">Finer work! We remove etched graffiti tags, scratches, mineral deposits, and acid etched graffiti damage.</li>
      <li class="benefit--short">Edge expertise! We can repair even deep scratches as close as 20mm from the edge of the glass.</li>
      <li class="benefit--short">Save time and money! Typical savings of up to 80% over the cost of glass replacement, with zero downtime during repair.</li>
    </ul>

    <div class="abs back-contact">
      <div class="contact-row"><svg viewBox="0 0 12 12"><rect x="1" y="1" width="10" height="10" rx="2" fill="#fff"/><path d="M4,3 Q3,6 6,9 L8,8 L7,6.5 L6,7 Q5,6 5,4.5 L5.6,4 Z" fill="#0c4670"/></svg>0800 555 0142</div>
      <div class="contact-row"><svg viewBox="0 0 12 12"><circle cx="6" cy="6" r="5" fill="none" stroke="#fff" stroke-width="1.4"/><path d="M1,6 H11 M6,1 V11" stroke="#fff" stroke-width="1"/></svg>www.lumenglasscare.co.uk</div>
    </div>

    <div class="abs badge" style="left:354px;top:272px">After repair<br>Clear as new!</div>

    <p class="abs coupon">
      <span class="coupon__save">Save 20%</span> <span class="coupon__off">off</span> our regular prices<br>
      for scratch repair, restoration, and etched graffiti removal.
      <span class="coupon__expiry">Act now – offer expires</span>
    </p>
  </section>

</main>
</body>
</html>
```